Need Business Card for eLearning Company

Need a business card designed for our company, CareerPathlane.

CareerPathlane has developed a complete 12 lesson eLearning course to teach you the skills you need to present yourself in a job interview. The course uses advanced learning techniques in the multimedia videos, plus contains quizzes and additional exercises to insure you get the course and can walk into any interview with confidence and ease, and get the job.

www.careerpathlane-demo.com

Attached is our logo

Industry/Entity Type

Business

```html
<!DOCTYPE html>
<html lang="en">
<head>
<meta charset="utf-8">
<title>CareerPathlane Business Card</title>
<link href="https://fonts.googleapis.com/css2?family=Roboto+Condensed:wght@300;400;700&display=swap" rel="stylesheet">
<style>
  :root {
    --page-bg: #ecebe8;
    --card-white: #ffffff;
    --ink-dark: #2b2b2b;
    --ink-grey: #6a6a6a;
    --brand-purple: #8e1a7c;
    --brand-magenta: #c13bb0;
    --brand-magenta-deep: #8f1f84;
    --brand-green: #8dbb27;
    --rule-light: rgba(255,255,255,0.55);
  }
  * { box-sizing: border-box; margin: 0; padding: 0; }
  html, body {
    width: 1200px; height: 1024px; overflow: hidden;
    background: var(--page-bg);
    font-family: "Roboto Condensed", "Arial Narrow", sans-serif;
  }
  .sheet { position: relative; width: 1200px; height: 1024px; }

  .card {
    position: absolute;
    width: 560px; height: 320px;
    border-radius: 4px;
    box-shadow: 0 6px 18px rgba(0,0,0,0.12);
    overflow: hidden;
  }

  /* Front */
  .card-front { left: 60px; top: 180px; background: var(--card-white); }
  .bubble-art {
    position: absolute; right: 34px; top: 22px;
    width: 270px; height: 150px; border-radius: 70px;
    background: radial-gradient(circle at 35% 45%, rgba(141,187,39,0.55), rgba(142,26,124,0.35) 60%, rgba(142,26,124,0.08) 100%);
  }
  .front-brand {
    position: absolute; left: 40px; top: 150px;
    display: flex; align-items: center; gap: 12px;
  }
  .brand-dot { width: 26px; height: 26px; border-radius: 50%; background: var(--brand-purple); }
  .front-brand .brand-name {
    font-size: 30px; font-weight: 300; color: var(--ink-grey); letter-spacing: 0.5px;
  }
  .holder-name {
    position: absolute; left: 40px; top: 200px;
    font-size: 26px; font-weight: 400; color: var(--ink-dark);
  }
  .holder-title {
    position: absolute; left: 40px; top: 232px;
    font-size: 16px; font-weight: 400; color: var(--brand-purple);
  }
  .contact-list {
    position: absolute; left: 40px; top: 260px;
    list-style: none;
  }
  .contact-list li {
    display: flex; align-items: center; gap: 10px;
    font-size: 13px; color: var(--ink-grey); height: 17px;
  }
  .contact-list svg { width: 12px; height: 12px; flex: none; }

  /* Back */
  .card-back {
    left: 580px; top: 540px;
    background: radial-gradient(ellipse at 60% 35%, var(--brand-magenta), var(--brand-magenta-deep) 110%);
  }
  .back-site {
    position: absolute; left: 26px; top: 32px;
    writing-mode: vertical-rl;
    font-size: 11px; letter-spacing: 5px; color: #fff; font-weight: 400;
  }
  .back-rule {
    position: absolute; left: 52px; top: 0; bottom: 0; width: 1px;
    background: var(--rule-light);
  }
  .back-brand {
    position: absolute; left: 130px; top: 128px;
    display: flex; align-items: center; gap: 14px;
  }
  .back-brand .brand-dot { background: #fff; width: 30px; height: 30px; }
  .back-brand .brand-name {
    font-size: 44px; font-weight: 300; color: #fff; letter-spacing: 0.5px;
  }
  .back-underline {
    position: absolute; left: 130px; top: 192px; width: 330px; height: 1px;
    background: var(--rule-light);
  }
</style>
</head>
<body>
<main class="sheet">
  <section class="card card-front">
    <div class="bubble-art" role="img" aria-label="Cluster of purple and green speech bubbles"></div>
    <div class="front-brand">
      <span class="brand-dot"></span>
      <span class="brand-name">CareerPathlane</span>
    </div>
    <h1 class="holder-name">Daniel R Whitford</h1>
    <p class="holder-title">Managing Director</p>
    <ul class="contact-list">
      <li>
        <svg viewBox="0 0 12 12"><path d="M2.5 1 L4.5 1 L5 3.5 L3.8 4.5 Q5 7 7.5 8.2 L8.5 7 L11 7.5 L11 9.5 Q10.5 11 9 11 Q1 10 1 3 Q1 1.5 2.5 1Z" fill="var(--brand-green)"/></svg>
        555-014-0199
      </li>
      <li>
        <svg viewBox="0 0 12 12"><rect x="1" y="2.5" width="10" height="7" rx="1" fill="var(--brand-green)"/><path d="M1.5 3 L6 6.5 L10.5 3" stroke="#fff" stroke-width="1" fill="none"/></svg>
        daniel@careerpathlane-demo.com
      </li>
      <li>
        <svg viewBox="0 0 12 12"><circle cx="6" cy="6" r="5" fill="var(--brand-green)"/><path d="M1 6 H11 M6 1 Q3 6 6 11 M6 1 Q9 6 6 11" stroke="#fff" stroke-width="0.8" fill="none"/></svg>
        www.careerpathlane-demo.com
      </li>
    </ul>
  </section>

  <section class="card card-back">
    <p class="back-site">WWW.CAREERPATHLANE-DEMO.COM</p>
    <div class="back-rule"></div>
    <div class="back-brand">
      <span class="brand-dot"></span>
      <span class="brand-name">CareerPathlane</span>
    </div>
    <div class="back-underline"></div>
  </section>
</main>
</body>
</html>
```